Greek God inspired Air Freshen needs Foil Package Design

We are Hall of Zephyra. We sell car air fresheners inspired by Ancient Greece. We currently sell 5 proprietary scents. You can see them here: https://www.shopvendra.com/Freshener-Natural-Essential-Hall-Zephyra/dp/K7R2QQWN4M
These are luxury air fresheners sold in awesome packages. 100% essential oils blended and bottled in the USA.
We need your help! We want to sell an additional line of scents. This line will be called "The Lyra Series" - or, The Lyra Series by Hall of Zephyra. This collection's theme will be - "The aromas you love, refined on high."
These new products will be takes on well know colognes and perfumes.
We will start with 3 new products:
Talvor – inspired by Brimara by Vask
Menthile – inspired by Ferolin by Lune
Pelion – inspired by Ombra by Tessin
Our original 5 products are packaged in tubes and bottled in a luxury black 8ml bottle (see attached and the link above). The "Lyra Series" will also have the same bottles, BUT, we want to package them in MYLAR FOIL BAGS. They will be 10x7cm (template attached).
What we need from you guys .... 3 designs. Front of the bag ONLY. One for each:
You have free reign, however the following items must be met:
The designs must be min 300 dpi.
Must include: "Lyra Series by Hall of Zephyra"
Must include: Hall of Zephyra Logo (attached)
Must include the words: "Car Air Fresheners"
Must marry well with our current imagery: https://www.shopvendra.com/Freshener-Natural-Essential-Hall-Zephyra/dp/K7R2QQWN4M
Don't necessarily need to mention the cologne that our product is inspired by, however, perhaps consider use some fonts/pattern/s shadows of the Vask/Brimara bottle "shape" as an example.
Keep in mind, you are only designing the front of the packages. We will complete the back. The back will have the brand story, instructions, UPC, ingredients.
Our thoughts on using foil mylar bags: 1. We sell online 2. They will stand out from the others 3. Gives you/designer more space/opportunity to convey the product/message 4. We believe mock-ups/photos of the bags will look great on our listing
Please contact with any questions.

```html
<!DOCTYPE html>
<html lang="en">
<head>
<meta charset="UTF-8">
<title>Menthile – Lyra Series – Hall of Zephyra</title>
<link rel="stylesheet" href="https://fonts.googleapis.com/css2?family=EB+Garamond:wght@400&family=Josefin+Sans:wght@300;400&display=swap">
<style>
  :root {
    --page-bg: #e8e8e8;
    --pouch-black: #050607;
    --pouch-deep: #0b1217;
    --pouch-blue: #1b3a4f;
    --pouch-teal: #2b5670;
    --ink-light: #d9dcde;
    --ink-soft: #b9bec2;
  }
  html, body {
    margin: 0;
    padding: 0;
    width: 1200px;
    height: 1001px;
    overflow: hidden;
    background: var(--page-bg);
  }
  .canvas {
    position: relative;
    width: 1200px;
    height: 1001px;
  }
  .pouch-front {
    position: absolute;
    left: 304px;
    top: 176px;
    width: 592px;
    height: 660px;
    background: var(--pouch-black);
    overflow: hidden;
  }
  .pouch-photo {
    position: absolute;
    inset: 0;
    background:
      radial-gradient(ellipse 70% 55% at 12% 95%, var(--pouch-teal) 0%, rgba(43,86,112,0.55) 35%, rgba(11,18,23,0) 75%),
      radial-gradient(ellipse 60% 70% at 30% 75%, rgba(27,58,79,0.7) 0%, rgba(11,18,23,0) 70%),
      linear-gradient(180deg, var(--pouch-black) 0%, var(--pouch-deep) 55%, #10222e 100%);
  }
  .pouch-copy {
    position: absolute;
    left: 0;
    right: 0;
    top: 0;
    bottom: 0;
    transform: translateX(-36px);
    text-align: center;
    color: var(--ink-light);
  }
  .category {
    position: absolute;
    left: 0;
    right: 0;
    top: 228px;
    margin: 0;
    font-family: "EB Garamond", serif;
    font-size: 17px;
    line-height: 22px;
    letter-spacing: 0.5px;
    color: var(--ink-soft);
  }
  .scent-name {
    position: absolute;
    left: 0;
    right: 0;
    top: 326px;
    margin: 0;
    font-family: "Josefin Sans", sans-serif;
    font-weight: 300;
    font-size: 44px;
    line-height: 52px;
    letter-spacing: 3px;
    color: var(--ink-light);
  }
  .series-name {
    position: absolute;
    left: 0;
    right: 0;
    top: 426px;
    margin: 0;
    font-family: "EB Garamond", serif;
    font-size: 23px;
    line-height: 28px;
    letter-spacing: 0.5px;
    color: var(--ink-light);
  }
  .brand-name {
    position: absolute;
    left: 0;
    right: 0;
    top: 596px;
    margin: 0;
    font-family: "Josefin Sans", sans-serif;
    font-weight: 400;
    font-size: 9px;
    letter-spacing: 1px;
    color: var(--ink-soft);
  }
</style>
</head>
<body>
  <main class="canvas">
    <section class="pouch-front">
      <div class="pouch-photo" role="img" aria-label="Moody dark photograph fading into deep blue tones at the lower left"></div>
      <div class="pouch-copy">
        <p class="category">CAR AIR<br>FRESHENERS</p>
        <h1 class="scent-name">MENTHILE</h1>
        <p class="series-name">LYRA SERIES</p>
        <p class="brand-name">HALL OF ZEPHYRA</p>
      </div>
    </section>
  </main>
</body>
</html>
```